WWW.VELTRONA.IT BUSINNES CARD

WE NEED A BUSINESS CARD . I HAVE A COMPANY IN ITALY NR 1 IN HAIR MEDICAL CARE AN HAIR REPLECEMENT . IN CARD I NEED WRITE WEB ADDRESS, MAIL , ADDRESS, TELEPHONE NUMBER , AND NAME
IN THE BACK SIDE I NEED MY DOCTOR LOGO .
MY WEB SITE IS WWW.VELTRONA.IT
Updates

Target Market(s)

CONSUMER B2C

Industry/Entity Type

Hair And Beauty

Contact Information for Business Card

I WANT A MEDICAL BUSINESS CARD.

Font styles to use
Other font styles liked:
• VERDANA

Colors
33a6d7
3176b5
85abd2
aedbee
eaf1f7
ffffff

Requirements
Must have
• I NEED MY LOGO AND LOGO OF DR VELTRONA

```html
<!DOCTYPE html>
<html lang="it">
<head>
<meta charset="utf-8">
<title>Veltrona – Business Card</title>
<link href="https://fonts.googleapis.com/css2?family=Roboto:wght@400;500&family=Work+Sans:wght@400;500&display=swap" rel="stylesheet">
<style>
  :root {
    --stage: #2b2b2d;
    --navy: #0b5394;
    --sky: #1fb1e3;
    --paper: #ffffff;
    --ink: #3a3a3a;
    --hair-dark: #6b3416;
    --hair-light: #c4744a;
    --skin: #f2b79a;
  }
  * { margin: 0; padding: 0; box-sizing: border-box; }
  html, body { width: 1200px; height: 930px; overflow: hidden; background: var(--stage); }
  .canvas { position: relative; width: 1200px; height: 930px; }

  .card-back {
    position: absolute; left: 85px; top: 148px; width: 363px; height: 634px;
    background: var(--navy);
  }
  .mascot-area {
    position: absolute; left: 49px; top: 58px; width: 205px; height: 518px;
    border-radius: 50% 50% 48% 48% / 30% 30% 12% 12%;
    background: linear-gradient(180deg, var(--hair-dark) 0%, #8a4a26 55%, var(--hair-light) 80%, var(--skin) 100%);
  }
  .doctor-mark {
    position: absolute; left: 265px; top: 425px;
    transform: translate(-50%, -50%) rotate(-90deg);
    font-family: "Work Sans", Verdana, sans-serif; font-weight: 500;
    font-size: 32px; color: var(--paper); white-space: nowrap;
  }

  .card-front {
    position: absolute; left: 482px; top: 419px; width: 633px; height: 363px;
    background: var(--paper); overflow: hidden;
    font-family: "Work Sans", Verdana, sans-serif; color: var(--ink);
  }
  .brand { position: absolute; left: 42px; top: 40px; }
  .brand-name {
    display: flex; align-items: center; gap: 10px;
    font-size: 34px; font-weight: 500; color: var(--navy); line-height: 1;
  }
  .brand-dot { width: 26px; height: 26px; border-radius: 50%; background: var(--sky); }
  .brand-tagline { margin-top: 8px; font-size: 9.5px; letter-spacing: .2px; color: var(--navy); }

  .person { position: absolute; right: 30px; top: 178px; text-align: right; }
  .person-name { font-family: "Roboto", Arial, sans-serif; font-weight: 500; font-size: 25px; color: var(--navy); line-height: 1.1; }
  .person-role { font-size: 16px; margin-top: 4px; color: #555; }

  .divider { position: absolute; left: 26px; right: 30px; top: 243px; height: 2px; background: var(--navy); }

  .contacts { position: absolute; left: 27px; top: 264px; list-style: none; font-size: 16px; line-height: 21px; letter-spacing: .4px; }
  .contacts li { display: flex; align-items: center; gap: 10px; }
  .contacts svg { width: 11px; height: 11px; fill: none; stroke: var(--navy); stroke-width: 1.6; }
  .contacts .strong { color: var(--navy); font-weight: 500; }

  .address { position: absolute; right: 30px; top: 264px; text-align: right; font-size: 16px; line-height: 21px; letter-spacing: .4px; }

  .bands { position: absolute; left: 0; bottom: 0; width: 633px; height: 40px; }
</style>
</head>
<body>
<div class="canvas">

  <section class="card-back" aria-label="Back side">
    <div class="mascot-area" role="img" aria-label="Cartoon doctor mascot: a strand of hair wearing a white coat and tie, giving a thumbs up"></div>
    <div class="doctor-mark">dr. Veltrona</div>
  </section>

  <section class="card-front" aria-label="Front side">
    <div class="brand">
      <div class="brand-name"><span class="brand-dot"></span>Veltrona</div>
      <div class="brand-tagline">CURA E REINTEGRAZIONE DEI CAPELLI</div>
    </div>

    <div class="person">
      <div class="person-name">DANIEL REYES</div>
      <div class="person-role">Director</div>
    </div>

    <div class="divider"></div>

    <ul class="contacts">
      <li><svg viewBox="0 0 12 12"><path d="M3 1.5 L5 4 L4 5.5 Q5 7.5 6.5 8 L8 7 L10.5 9 L9 10.8 Q4 10 1.5 3 Z"/></svg>0203 555 0147</li>
      <li><svg viewBox="0 0 12 12"><rect x="1" y="2.5" width="10" height="7"/><path d="M1 2.5 L6 6.5 L11 2.5"/></svg>info@veltrona.it</li>
      <li><svg viewBox="0 0 12 12"><circle cx="6" cy="6" r="4.8"/><path d="M1.2 6 H10.8 M6 1.2 Q3 6 6 10.8 Q9 6 6 1.2"/></svg><span>www.<span class="strong">veltrona</span>.it</span></li>
    </ul>

    <div class="address">1287 Marlow Street<br>Harrisburg, PA 17101</div>

    <svg class="bands" viewBox="0 0 633 40" aria-hidden="true">
      <polygon points="0,26 346,26 334,40 0,40" fill="var(--sky)"/>
      <polygon points="375,0 633,0 633,40 338,40" fill="var(--navy)"/>
    </svg>
  </section>

</div>
</body>
</html>
```